International Used Food Processing Equipment company needs an awesome website!

We have been in business now for more than 15 years, and we are now launching a new website where international and USA based customers can view photos, descriptions, and ask questions of industrial food processing equipment.

We want the site to be vibrant and but yet communicate a professional tone to our customers. Most of our customers are older males, and the site must be easy to navigate, with easy on the eye color scheme. We want to features a lot of photos and a excellent equipment descriptions, with links where visitors can click on an item to send us a request for more information. We require easy to read font, clear navigation buttons and clear contact information to be found on each page.

Some of our competitors sites:
www.KVPTrade.com
www.lantorvalleyworks.com
www.pelvoxgroup.com

Our business name and logo is attached, but this is a rending of an image that was made about 10 years ago. Please let us know if you have any questions.

Target Market(s)

Food processing companies (canneries, fresh cut sector, large catering companies) in the USA and South America.

Logo Text

Excellent Machines at Excellent Prices

Coding

Coded - Design and coding required

Number of Pages Required

5+ page

Colors

Designer to choose colors to be used in the design.

Requirements
Must have
• Easy to navigate photo galleries, easy category search and easy machine search by keywords.
• Event Calendar
• Sign-up page for email newsletter
Nice to have
• Blog feature or latest news
• Past projects page
Should not have
• Hard to read font

```html
<!DOCTYPE html>
<html lang="en">
<head>
<meta charset="utf-8">
<title>Foodline Depot – Used Food Processing Equipment</title>
<link href="https://fonts.googleapis.com/css2?family=Open+Sans:wght@400;600;700&display=swap" rel="stylesheet">
<style>
:root{
  --blue:#3a8fd6;
  --blue-dark:#2f7cc0;
  --yellow:#f9a81a;
  --ink:#333;
  --muted:#777;
  --dark:#3b3b3b;
  --darker:#2b2b2b;
  --line:#e4e4e4;
  --white:#fff;
}
*{box-sizing:border-box;margin:0;padding:0}
html,body{width:1200px;height:1200px;overflow:hidden;background:#fff;font-family:'Open Sans',Arial,sans-serif;color:var(--ink)}
.page{position:absolute;left:414px;top:0;width:467px;height:1500px;transform:scale(.8);transform-origin:0 0;overflow:hidden;background:#fff}
.abs{position:absolute}
.topbar{left:0;top:0;width:467px;height:12px;background:var(--darker);color:#ccc;font-size:3.6px;display:flex;align-items:center;padding:0 62px;gap:10px}
.topbar .social{margin-left:auto;display:flex;gap:3px}
.topbar .social i{width:4px;height:4px;background:#bbb;display:block}
.logo{left:62px;top:19px;font-weight:700;color:var(--ink);font-size:11px;line-height:1;letter-spacing:.3px}
.logo small{display:block;font-size:4px;color:var(--blue);font-weight:700;letter-spacing:.2px;margin-top:2px}
.hsearch{left:302px;top:22px;width:102px;height:15px;border:1px solid var(--line);background:#fafafa;font-size:3.5px;color:#aaa;padding:5px 4px}
.nav{left:62px;top:47px;width:280px;height:19px;background:var(--dark);display:flex;align-items:center;gap:9px;padding-left:8px;color:#fff;font-size:3.6px;font-weight:600;z-index:2}
.quote{left:318px;top:47px;width:149px;height:19px;background:var(--blue);clip-path:polygon(12px 0,100% 0,100% 100%,0 100%);color:#fff;font-size:4.4px;font-weight:700;display:flex;align-items:center;padding-left:30px;z-index:2}
.hero{left:0;top:57px;width:467px;height:191px;background:radial-gradient(ellipse at 45% 40%,#8a7a52,#4a4334 55%,#2a2824)}
.frame{left:113px;top:124px;width:239px;height:52px;border:1.5px solid #fff;border-top:none;border-bottom:none}
.frame::before,.frame::after{content:"";position:absolute;left:0;width:8px;height:1.5px;background:#fff}
.hero-title{left:100px;top:123px;width:265px;text-align:center;color:#fff;font-weight:700;font-size:10.5px;line-height:14px}
.hero-title b{color:var(--yellow)}
.hero-search{left:135px;top:163px;width:148px;height:18px;background:#eee;font-size:3.6px;color:#999;padding:6px 5px}
.hero-btn{left:283px;top:163px;width:47px;height:18px;background:var(--blue);color:#fff;font-size:5px;font-weight:600;text-align:center;line-height:18px}
.arrow{top:143px;width:12px;height:20px;background:var(--blue)}
.h2{font-size:8px;color:var(--ink);font-weight:400;letter-spacing:.2px}
.h2 b{color:var(--blue);font-weight:700}
.h2.u{border-bottom:1px solid #bbb;padding-bottom:1px}
.dots{left:388px;top:269px;display:flex;gap:2px}
.dots i{width:3.5px;height:3.5px;border-radius:50%;background:#ddd;display:block}
.dots i:last-child{background:var(--yellow)}
.card{width:82px}
.card .t{font-size:3.8px;font-weight:600;background:#f3f3f3;padding:3px 5px;height:10px}
.card .img{height:54px;margin-top:2px}
.card p{font-size:3.4px;color:var(--muted);line-height:5.5px;margin-top:5px;height:22px}
.card .btn{display:inline-block;background:var(--blue);color:#fff;font-size:3.4px;padding:3px 5px;margin-top:2px}
.news{left:0;top:414px;width:467px;height:32px;background:var(--yellow)}
.news-title{left:62px;top:424px;color:#fff;font-weight:700;font-size:8.5px;letter-spacing:.3px}
.news-input{left:236px;top:423px;width:110px;height:15px;background:#fff;font-size:3.5px;color:#aaa;padding:5px 4px;border:1px solid #f2d08a}
.news-btn{left:348px;top:423px;width:56px;height:15px;background:#111;color:#fff;font-size:4.5px;font-weight:700;text-align:center;line-height:15px}
.years{left:0;top:446px;width:467px;height:172px;background:linear-gradient(90deg,#1f1d1c,#3a332c 60%,#2a2420)}
.years-h{left:62px;top:461px;color:#fff;font-size:8px}
.years-h b{color:var(--yellow);font-weight:700}
.years-p{left:62px;width:172px;color:#ddd;font-size:3.6px;line-height:6.5px}
.years-btn{left:62px;top:582px;width:69px;height:18px;background:var(--blue);color:#fff;font-size:3.8px;text-align:center;line-height:18px}
.years-img{left:250px;top:465px;width:152px;height:133px;border:2px solid #e8e0d0;background:radial-gradient(circle at 70% 35%,#e5e2da,#9b8f78 45%,#5c4d36)}
.g{width:100px;height:105px}
.zoom{left:41px;top:43px;width:20px;height:20px;border-radius:50%;background:#fff}
.ind{left:0;top:906px;width:467px;height:277px;background:linear-gradient(180deg,#3f95d8,#3488cc 60%,#2f7fc2)}
.center{left:0;width:467px;text-align:center}
.ind-h{color:#fff;font-size:8px}
.ind-h b{color:#111;font-weight:700}
.ind-p{color:#dbeaf7;font-size:3.6px;line-height:7.5px;padding:0 136px}
.ind-box{top:976px;width:61px;height:56px;background:rgba(255,255,255,.35);padding:4px}
.ind-box div{background:#f4f4f4;height:100%;display:flex;align-items:center;justify-content:center;text-align:center;font-size:3.8px;font-weight:600;color:#444}
.cal{left:110px;top:1070px;width:247px;height:99px;background:#fff;border:1px solid #cfd8e0}
.blog-h{color:var(--ink);font-size:8px}
.blog-h b{color:var(--blue);font-weight:700}
.blog-p{color:var(--muted);font-size:3.6px;line-height:7.5px;padding:0 115px}
.post{top:1247px;height:110px}
.post .ov{position:absolute;left:6px;bottom:5px;right:6px;color:#fff}
.post .ov h4{font-size:5.4px;font-weight:400}
.post .ov p{font-size:3.2px;line-height:5.5px;margin-top:2px;color:#eee}
.post .ov span{font-size:3px;color:var(--yellow)}
.footer{left:0;top:1375px;width:467px;height:107px;background:#444}
.fcol{top:1388px;color:#ddd;font-size:3.6px;line-height:8px}
.fcol h5{font-size:5.5px;color:#fff;font-weight:600;margin-bottom:5px}
.fin{width:92px;height:8px;background:#fff;font-size:3px;color:#999;padding:2px 3px;margin-bottom:3px}
.fsub{background:var(--yellow);color:#fff;font-size:3.2px;width:35px;height:9px;text-align:center;line-height:9px}
.copy{left:0;top:1482px;width:467px;height:18px;background:#333;color:#bbb;font-size:3.4px;text-align:center;line-height:18px}
</style>
</head>
<body>
<div class="page">
  <div class="abs topbar"><span>☎ +1 555 010 2233</span><span>✉ hello@foodlinedepot.com</span><span class="social"><i></i><i></i><i></i><i></i></span></div>

  <div class="abs logo">FOODLINE DEPOT<small>EXCELLENT MACHINES AT EXCELLENT PRICES</small></div>
  <div class="abs hsearch">Search Categories...</div>

  <div class="abs hero" role="img" aria-label="Industrial food processing plant with a large mixing vat"></div>
  <div class="abs nav"><span>HOME</span><span>ABOUT US</span><span>COMPANY</span><span>SERVICES</span><span>EQUIPMENTS</span><span>BLOG</span><span>INDUSTRIES</span><span>CONTACT US</span></div>
  <div class="abs quote">✎&nbsp; GET A FREE QUOTE</div>

  <div class="abs frame"></div>
  <div class="abs hero-title">WE HAVE BEEN IN BUSINESS NOW FOR<br>MORE THAN <b>15 YEARS</b></div>
  <div class="abs hero-search">Search our inventory by equipment...</div>
  <div class="abs hero-btn">SEARCH</div>
  <div class="abs arrow" style="left:0"><svg width="12" height="20"><path d="M7 7 4 10 7 13" stroke="#fff" fill="none" stroke-width="1.2"/></svg></div>
  <div class="abs arrow" style="left:455px"><svg width="12" height="20"><path d="M5 7 8 10 5 13" stroke="#fff" fill="none" stroke-width="1.2"/></svg></div>

  <div class="abs h2 u" style="left:62px;top:263px">PROVIDE <b>SERVICES</b></div>
  <div class="abs dots"><i></i><i></i><i></i></div>

  <div class="abs card" style="left:62px;top:289px"><div class="t">COMPLETE LINES</div><div class="img" role="img" aria-label="Complete stainless processing line" style="background:linear-gradient(135deg,#c9ced4,#6e7680)"></div><p>We perform or supervise every step of your project from assembly to final commissioning.</p><span class="btn">Read More</span></div>
  <div class="abs card" style="left:148px;top:289px"><div class="t">INDUSTRIAL EQUIPMENT</div><div class="img" role="img" aria-label="Industrial pipework and machinery" style="background:linear-gradient(135deg,#d8d4cc,#7c7a74)"></div><p>Staff of engineers specialized in powder handling on your production site to optimize your process line.</p><span class="btn">Read More</span></div>
  <div class="abs card" style="left:235px;top:289px"><div class="t">PACKAGING EQUIPMENTS</div><div class="img" role="img" aria-label="Packaging machine with film rolls" style="background:linear-gradient(135deg,#e3e3e3,#8a8c90)"></div><p>The test centre Foodline Depot Process has been built for all of our industrial customers to define the</p><span class="btn">Read More</span></div>
  <div class="abs card" style="left:321px;top:289px"><div class="t">PROCESSING EQUIPMENTS</div><div class="img" role="img" aria-label="Stainless steel processing tanks" style="background:linear-gradient(135deg,#d6dde6,#7d8a9a)"></div><p>The Foodline Depot coordinates all services to handle your whole project from pre-study to operations.</p><span class="btn">Read More</span></div>

  <div class="abs news"></div>
  <div class="abs news-title">SIGN UP OUR NEWSLETTER</div>
  <svg class="abs" style="left:210px;top:425px" width="16" height="10"><path d="M1 1 5 5 1 9M6 1 10 5 6 9M11 1 15 5 11 9" stroke="#fde3b0" fill="none" stroke-width="1.2"/></svg>
  <div class="abs news-input">Enter your email id</div>
  <div class="abs news-btn">SUBSCRIBE</div>

  <div class="abs years"></div>
  <div class="abs years-h">15+ YEARS <b>IN BUSINESS</b></div>
  <div class="abs years-p" style="top:481px">Our many years of experience in food and feed, chemical and fine chemical processing industries, water treatment and building industry allow us to offer you the benefits of inter-sector synergy.</div>
  <div class="abs years-p" style="top:507px">Our industrial workshop allows you to perform tests on our test plant and guarantees the success of your project and the reliability of your production line. Our human size structure offers excellent flexibility and reactivity with competitive budgets.</div>
  <div class="abs years-p" style="top:542px">Our industrial workshop allows you to perform tests on our test plant and guarantees the success of your project and the reliability of your production line.</div>
  <div class="abs years-btn">View All Past Projects</div>
  <div class="abs years-img" role="img" aria-label="Pressure gauge on processing pipework"></div>
  <div class="abs dots" style="left:319px;top:585px"><i style="background:#fff"></i><i style="background:#fff"></i><i></i></div>

  <div class="abs h2 u" style="left:62px;top:632px">FEATURED <b>GALLERY</b></div>
  <div class="abs g" style="left:62px;top:657px;background:linear-gradient(135deg,#c24a22,#5b2a1c)" role="img" aria-label="Red sorting conveyor with produce"><div class="abs zoom"><svg width="20" height="20"><circle cx="9" cy="9" r="3" stroke="#333" fill="none" stroke-width="1.2"/><path d="M11 11 14 14" stroke="#333" stroke-width="1.4"/></svg></div></div>
  <div class="abs g" style="left:183px;top:657px;background:linear-gradient(135deg,#cfe2f0,#3f7fb8)" role="img" aria-label="Food plant worker in protective clothing"></div>
  <div class="abs g" style="left:303px;top:657px;background:linear-gradient(135deg,#d69a52,#6b4a2a)" role="img" aria-label="Baked buns on a production line"></div>
  <div class="abs g" style="left:62px;top:783px;background:linear-gradient(135deg,#f48a2a,#c4531a)" role="img" aria-label="Gloved hand sorting oranges"></div>
  <div class="abs g" style="left:183px;top:783px;background:linear-gradient(135deg,#b9c6d2,#4a86c4)" role="img" aria-label="Blue pipes in a processing plant"></div>
  <div class="abs g" style="left:303px;top:783px;background:linear-gradient(135deg,#c4ccd6,#5b6774)" role="img" aria-label="Row of stainless steel tanks"></div>

  <div class="abs ind" role="img" aria-label="Blue tinted industrial skyline"></div>
  <div class="abs center ind-h" style="top:920px"><span class="h2 u" style="color:#fff">INDUSTRIES WE <b style="color:#111">SERVE</b></span></div>
  <div class="abs center ind-p" style="top:939px">The Foodline Depot Process is "The smartest designer for powder handling solutions" for bulk handling system and the realization of your production lines from conception to commissioning internationally.</div>
  <div class="abs ind-box" style="left:130px"><div>CANNERIES</div></div>
  <div class="abs ind-box" style="left:203px"><div>FRESH CUT<br>SECTOR</div></div>
  <div class="abs ind-box" style="left:276px"><div>CATERING<br>COMPANIES</div></div>
  <div class="abs center" style="top:1046px"><span class="h2 u" style="color:#fff">LATEST <b style="color:#111">EVENTS</b></span></div>

  <div class="abs cal">
    <svg width="245" height="97" font-family="Open Sans,sans-serif" font-size="2.6" fill="#555">
      <rect x="2" y="3" width="42" height="42" fill="#fff" stroke="#ccc" stroke-width=".4"/>
      <text x="13" y="7">October 2017</text>
      <rect x="2" y="10" width="42" height="29" fill="#fff8e8"/>
      <rect x="2" y="49" width="42" height="44" fill="#fff" stroke="#ccc" stroke-width=".4"/>
      <text x="12" y="53">November 2017</text>
      <rect x="46" y="3" width="20" height="5" fill="#f08a2a"/>
      <rect x="66" y="3" width="10" height="5" fill="#eee"/>
      <text x="62" y="7" fill="#333">Today</text>
      <rect x="46" y="12" width="197" height="82" fill="#fff" stroke="#ccc" stroke-width=".4"/>
      <path d="M46 15H243M46 46H243M46 78H243M80 12V94M114 12V94M148 12V94M183 12V94M217 12V94" stroke="#ddd" stroke-width=".4"/>
      <text x="48" y="14.5">Sunday</text><text x="82" y="14.5">Monday</text><text x="116" y="14.5">Tuesday</text><text x="150" y="14.5">Wednesday</text><text x="185" y="14.5">Thursday</text><text x="219" y="14.5">Friday</text>
      <rect x="80" y="25" width="103" height="5" fill="#fde7a6"/><text x="82" y="28.6">Event</text>
      <rect x="114" y="32" width="69" height="5" fill="#cfe7b8"/><text x="116" y="35.6">Event</text>
      <rect x="80" y="55" width="68" height="5" fill="#cfe0ee"/><text x="82" y="58.6">Event 1</text>
      <rect x="148" y="55" width="35" height="5" fill="#f4a7a7"/><text x="150" y="58.6">Event 4</text>
    </svg>
  </div>

  <div class="abs center blog-h" style="top:1198px"><span class="h2 u">LATEST <b>BLOG</b></span></div>
  <div class="abs center blog-p" style="top:1219px">The Foodline Depot Process is "The smartest designer for powder handling solutions" for bulk handling system and the realization of your production lines from conception to commissioning internationally.</div>

  <div class="abs post" style="left:62px;width:101px;background:linear-gradient(180deg,#7fb35a,#3a4a2e 70%,#222)" role="img" aria-label="Rows of lettuce seedlings"><div class="ov"><h4>Blog Title Will be Here</h4><p>Our many years of experience in food and feed, chemical and fine chemical processing industries, water treatment and building industry</p><span>January 15, 2019</span></div></div>
  <div class="abs post" style="left:181px;width:105px;background:linear-gradient(180deg,#c9b083,#3a3a3a 70%,#1e1e1e)" role="img" aria-label="Gloved hands at a cutting table"><div class="ov"><h4>Blog Title Will be Here</h4><p>Our many years of experience in food and feed, chemical and fine chemical processing industries, water treatment and building industry</p><span>January 15, 2019</span></div></div>
  <div class="abs post" style="left:299px;width:105px;background:linear-gradient(180deg,#c9bfb5,#4a3e36 70%,#1e1e1e)" role="img" aria-label="Chef plating a dish"><div class="ov"><h4>Blog Title Will be Here</h4><p>Our many years of experience in food and feed, chemical and fine chemical processing industries, water treatment and building industry</p><span>January 15, 2019</span></div></div>

  <div class="abs footer"></div>
  <div class="abs fcol" style="left:62px"><h5>Industrial Sector</h5>Canneries<br>Fresh cut sector<br>Catering companies industry</div>
  <div class="abs fcol" style="left:144px"><h5>Quick Links</h5><div style="display:flex;gap:22px"><div>Home<br>About Us<br>Company<br>Services</div><div>Equipments<br>Blog<br>Industries<br>Contact us</div></div></div>
  <div class="abs fcol" style="left:225px;line-height:5.5px"><h5 style="margin-bottom:8px">Contact Us</h5>
    <div style="padding-left:10px;position:relative"><svg class="abs" style="left:0;top:0" width="5" height="6"><path d="M2.5 6 .6 3A2 2 0 1 1 4.4 3Z" fill="#fff"/></svg>14 Harbor Lane<br>Millbrook Park<br>Ridgeview 40210</div>
    <div style="padding-left:10px;position:relative;margin-top:3px"><svg class="abs" style="left:0;top:.5px" width="5" height="5"><rect x=".5" y=".5" width="4" height="4" rx="1" fill="#fff"/></svg>+1 555 010 2233</div>
    <div style="padding-left:10px;position:relative;margin-top:3px"><svg class="abs" style="left:0;top:1px" width="5" height="4"><rect width="5" height="3.5" fill="#fff"/></svg>hello@foodlinedepot.com</div>
  </div>
  <div class="abs fcol" style="left:312px"><h5>Get In Touch</h5><div class="fin">Name</div><div class="fin">Email</div><div class="fin" style="height:20px">Message</div><div class="fsub" style="margin-top:5px">Submit</div></div>
  <svg class="abs" style="left:62px;top:1450px" width="60" height="14"><g fill="#fff"><rect x="2" y="2" width="8" height="8" transform="rotate(45 6 6)"/><rect x="18" y="2" width="8" height="8" transform="rotate(45 22 6)"/><rect x="34" y="2" width="8" height="8" transform="rotate(45 38 6)"/><rect x="50" y="2" width="8" height="8" transform="rotate(45 54 6)"/></g></svg>
  <div class="abs copy">Copyright © 2019 The Foodline Depot - All rights reserved</div>
</div>
</body>
</html>
```